Quiet Lanterns: Reflections on Tide Charts and Orchard Rituals Among Coastal Villages.

Book cover, spine, and back cover. This is written by Dr. T. HALVERSEN, and will be an educational book for academics, government officials, and the general population.
I'm imagining the outline of a person with am active mind in the middle. It would be overlayed on top of a circular galaxy on the background. On either side, smaller, perhaps in the background would be a cross on one side and a few uaps (ufo) of different shapes on the other (orb, saucer, triangle. ) beneath allnof this would be something symbolizing society - either the earth itself or the skyline of a large city.
By Dr. T. HALVERSEN along the bottom, i presume. (Ai cannot make this, but I've included a few examples nonetheless. )
I assume I will be given the opportunity to write a synopsis on the back cover. I will be self publishing and selling from my website.
Target Market(s)
Academics, professionals, church leaders, government officials, and the general public.
Industry/Entity Type
Professional and community education
Requirements
Must have
- It should look like a ph.d level book. Eye catching but not overly fantastical. (Its an educational book not a comic book)
Should not have
- Not hollywood or fantasy book looking. It should look a graduate school book. The tone is quite serious.

```html
<!DOCTYPE html>
<html lang="en">
<head>
<meta charset="UTF-8">
<title>Quiet Lanterns — Book Cover</title>
<link rel="stylesheet" href="https://fonts.googleapis.com/css2?family=Cinzel:wght@400;600;700&family=Montserrat:wght@400&display=swap">
<style>
  :root {
    --page: #ffffff;
    --ink-light: #ffffff;
    --ink-soft: #e8edf3;
    --navy-deep: #0e1720;
    --navy: #122230;
    --navy-blue: #0b2a42;
    --spine: #101b25;
    --glow-warm: #f3b35e;
    --glow-blue: #3f6f8c;
    --horizon: #c98a55;
  }
  * { box-sizing: border-box; margin: 0; padding: 0; }
  html, body { width: 1200px; height: 1200px; overflow: hidden; background: var(--page); }

  .book-wrap {
    position: absolute;
    left: 65px; top: 217px;
    width: 1071px; height: 765px;
    display: flex;
  }

  /* Back cover */
  .back-cover {
    position: relative;
    width: 509px; height: 100%;
    background: linear-gradient(180deg, var(--navy-deep) 0%, var(--navy) 55%, var(--navy-blue) 85%, #0a1a27 100%);
    color: var(--ink-light);
  }
  .back-landscape {
    position: absolute; left: 0; right: 0; bottom: 0; height: 190px;
    background: linear-gradient(180deg, rgba(12,40,62,0) 0%, rgba(8,28,44,0.85) 55%, rgba(7,20,30,1) 100%);
  }
  .back-title {
    position: absolute; left: 0; width: 509px; top: 26px;
    font-family: "Cinzel", serif; font-weight: 400;
    font-size: 54px; line-height: 54px; letter-spacing: 0.06em;
    text-align: center; padding-left: 10px;
  }
  .back-subtitle {
    position: absolute; left: 28px; width: 454px; top: 144px;
    font-family: "Cinzel", serif; font-weight: 700;
    font-size: 14.5px; line-height: 20px; letter-spacing: 0.03em;
    text-align: center; text-transform: uppercase;
  }
  .synopsis {
    position: absolute; left: 28px; width: 454px;
    font-family: "Montserrat", sans-serif; font-size: 10.6px; line-height: 16.5px;
    color: var(--ink-soft); text-align: justify;
  }
  .synopsis p + p { margin-top: 16px; }
  .synopsis-main { top: 193px; }
  .back-author {
    position: absolute; left: 0; width: 509px; top: 430px;
    font-family: "Cinzel", serif; font-weight: 400; font-size: 24px; letter-spacing: 0.04em;
    text-align: center;
  }
  .author-bio { top: 467px; }
  .isbn-box {
    position: absolute; left: 303px; top: 650px;
    width: 178px; height: 79px; background: var(--page);
  }

  /* Spine */
  .spine {
    position: relative; width: 51px; height: 100%;
    overflow: hidden;
    background: linear-gradient(180deg, var(--spine) 0%, #13222e 60%, #0e1822 100%);
    color: var(--ink-light);
  }
  .spine-title, .spine-author {
    position: absolute; left: 50%;
    writing-mode: vertical-rl;
    transform: translateX(-50%);
    font-family: "Cinzel", serif; font-weight: 400; white-space: nowrap;
  }
  .spine-title { top: 38px; font-size: 40px; letter-spacing: 0.04em; }
  .spine-author { bottom: 30px; font-size: 20px; letter-spacing: 0.03em; }

  /* Front cover */
  .front-cover {
    position: relative; width: 511px; height: 100%;
    overflow: hidden; color: var(--ink-light);
  }
  .front-art {
    position: absolute; inset: 0;
    background:
      radial-gradient(circle at 50% 46%, rgba(243,179,94,0.85) 0 18px, rgba(243,179,94,0.25) 60px, rgba(63,111,140,0.35) 150px, rgba(63,111,140,0) 170px),
      radial-gradient(ellipse 70% 14% at 50% 80%, rgba(201,138,85,0.55), rgba(201,138,85,0) 100%),
      radial-gradient(ellipse 60% 18% at 50% 100%, #24405a, rgba(36,64,90,0) 100%),
      linear-gradient(180deg, #0f1a24 0%, #142633 40%, #2a4556 70%, #1b2c3a 88%, #0d1822 100%);
  }
  .front-title {
    position: absolute; left: 0; width: 511px; top: 30px;
    font-family: "Cinzel", serif; font-weight: 400;
    font-size: 76px; line-height: 92px; letter-spacing: 0.05em;
    text-align: center;
  }
  .front-subtitle {
    position: absolute; left: 20px; width: 471px; top: 222px;
    font-family: "Cinzel", serif; font-weight: 700;
    font-size: 14.5px; line-height: 20px; letter-spacing: 0.03em;
    text-align: center; text-transform: uppercase;
  }
  .front-author {
    position: absolute; left: 0; width: 511px; top: 700px;
    font-family: "Cinzel", serif; font-weight: 400; font-size: 32px; letter-spacing: 0.04em;
    text-align: center;
  }
</style>
</head>
<body>
  <div class="book-wrap">
    <section class="back-cover">
      <div class="back-landscape" role="img" aria-label="Dim night landscape of distant hills under a deep blue sky"></div>
      <h2 class="back-title">QUIET<br>LANTERNS</h2>
      <p class="back-subtitle">Reflections on Tide Charts and Orchard Rituals Among Coastal Villages.</p>
      <div class="synopsis synopsis-main">
        <p>Lorem Ipsum is simply dummy text of the printing and typesetting industry. Lorem Ipsum has been the industry's standard dummy text ever since the 1500s, when an unknown printer took a galley of type and scrambled it to make a type specimen book. It has survived not only five centuries, but also the leap</p>
        <p>into electronic typesetting, remaining essentially unchanged. It was popularised in the 1960s with the release of Glyphsheet sheets containing Lorem Ipsum passages, and more recently with desktop publishing software like Folio Layout including versions of Lorem Ipsum. simply dummy text of the printing and.</p>
        <p>typesetting industry. Lorem Ipsum has been the industry's standard dummy text ever since the 1500s, when an unknown printer took a galley of type and scrambled it to make a type specimen book. It has survived not only five centuries, but also the leap</p>
      </div>
      <h3 class="back-author">DR. T. HALVERSEN</h3>
      <div class="synopsis author-bio">
        <p>Lorem Ipsum is simply dummy text of the printing and typesetting industry. Lorem Ipsum has been the industry's standard dummy text ever since the 1500s, when an unknown printer took a galley of type and scrambled it to make a type specimen book. It has survived not only five centuries, but also the leap into electronic typesetting, remaining essentially unchanged. It was popularised in the 1960s with the release of Glyphsheet sheets containing Lorem Ipsum passages, and more recently with desktop publishing software like Folio Layout including versions of Lorem Ipsum.</p>
      </div>
      <div class="isbn-box"></div>
    </section>

    <section class="spine">
      <span class="spine-title">QUIET LANTERNS</span>
      <span class="spine-author">DR. T. HALVERSEN</span>
    </section>

    <section class="front-cover">
      <div class="front-art" role="img" aria-label="Night-sky illustration: a silhouetted head in profile with a glowing mind and cross, a luminous circular halo, small flying craft, and a city skyline on the curve of the earth"></div>
      <h1 class="front-title">QUIET<br>LANTERNS</h1>
      <p class="front-subtitle">Reflections on Tide Charts and Orchard Rituals Among Coastal Villages.</p>
      <p class="front-author">DR. T. HALVERSEN</p>
    </section>
  </div>
</body>
</html>
```